Cultural Values, and Purpose, Vision and Mission statements design

We have recently created Cultural Values, and Purpose, Vision and Mission statements for a client’s business. We would like a visual representation created of each of these, to be hung on display in their office. For this project, we would like four (4) graphic design prints drawn up that depict:1. Purpose2. Vision3. Mission4. Cultural ValuesAll print designs should use a recurring, common theme, and be reflective of the business’ colours (see attached logo.)Please read and follow specifications in attached design brief.
Updates

Need extra days to review

Target Market(s)

Females, aged between 37 and 57 years old, who are family orientated, living locally, married and have between 1 and 3 children living at home.

Requirements
Must have
• Photoshop (PSD) format: All completed design will need to be in Photoshop (PSD) format before being handed over. This is to ensure that we can make alterations before printing if necessary.
• Quality: All designs must be 300 pixels resolution or higher.
• Purpose, Vision & Mission Designs Dimensions: The dimensions for each of the Purpose, Vision and Mission designs will need to be 30.5cm x 40.6cm (portrait, rectangle shape) with a surrounding 3.8cm border as it will be printed onto canvas matching these specifications.
• Cultural Values Dimensions: There are no specific dimensions required for the Cultural Values so the designer should feel free to display them best they see fit.
• Theme: All must follow the same theme and be reflective of the business's colours and logo.

```html
<!DOCTYPE html>
<html lang="en">
<head>
<meta charset="utf-8">
<title>Purpose, Vision, Mission and Cultural Values Prints</title>
<link rel="stylesheet" href="https://fonts.googleapis.com/css2?family=Oswald:wght@400;500&family=Open+Sans:wght@400;600;700&display=swap">
<style>
  :root {
    --backdrop: #606062;
    --paper: #ffffff;
    --grey: #8e8f92;
    --teal: #0f7e98;
    --orange: #ef8220;
    --shadow: #e3e3e4;
    --ink-grey: #8a8b8e;
  }
  * { margin: 0; padding: 0; box-sizing: border-box; }
  html, body { width: 1200px; height: 448px; overflow: hidden; background: var(--backdrop); }
  .print-set { position: relative; width: 1200px; height: 448px; }
  .print { position: absolute; top: 52px; width: 249px; height: 330px; background: var(--paper); }
  .print svg { display: block; width: 249px; height: 330px; }
  .print--purpose { left: 84px; --accent: var(--grey); }
  .print--vision { left: 351px; --accent: var(--teal); }
  .print--mission { left: 620px; --accent: var(--orange); }
  .print--values { left: 889px; --accent: var(--grey); }

  .accent-fill { fill: var(--accent); }
  .paper-fill { fill: var(--paper); }
  .shadow-fill { fill: var(--shadow); }
  .frame-line { fill: none; stroke: var(--paper); stroke-width: 1.1; }

  .heading { font-family: "Oswald", sans-serif; font-weight: 500; font-size: 21px; fill: var(--accent); }
  .heading-rule { stroke: var(--accent); stroke-width: 1.3; }
  .statement { font-family: "Open Sans", sans-serif; font-weight: 600; font-size: 5.4px; fill: var(--paper); }
  .statement--dense { font-size: 4.1px; }
  .values-list { font-family: "Open Sans", sans-serif; font-weight: 600; font-size: 6px; fill: var(--ink-grey); }
  .brand-name { font-family: "Open Sans", sans-serif; font-weight: 600; font-size: 8px; fill: var(--ink-grey); }
  .brand-mark { fill: var(--orange); }
  .handshake-badge { fill: #7fa9b2; }
</style>
</head>
<body>
<main class="print-set">

  <!-- Purpose -->
  <section class="print print--purpose" aria-label="Purpose">
    <svg viewBox="0 0 217 288" preserveAspectRatio="none">
      <rect class="accent-fill" x="0" y="0" width="217" height="232"/>
      <polygon class="paper-fill" points="149,0 161,0 145,52 133,52"/>
      <polygon class="paper-fill" points="0,52 150,52 133,110 0,110"/>
      <polygon class="paper-fill" points="97,175 109,175 92,232 80,232"/>
      <polygon class="paper-fill" points="0,206 103,206 96,232 0,232"/>
      <rect class="paper-fill" x="0" y="232" width="217" height="56"/>
      <polygon class="shadow-fill" points="183,70 190,66 140,288 124,288"/>
      <polygon class="paper-fill" points="190,66 217,150 217,288 138,288"/>
      <rect class="frame-line" x="7" y="7" width="203" height="274"/>
      <text class="heading" x="15" y="94">PURPOSE</text>
      <line class="heading-rule" x1="15" y1="100" x2="88" y2="100"/>
      <text class="statement" x="14" y="130">
        <tspan x="14">Providing vehicle safety and security</tspan>
        <tspan x="14" dy="7">to Gippsland families on our country</tspan>
        <tspan x="14" dy="7">roads.</tspan>
      </text>
      <rect class="brand-mark" x="118" y="266" width="8" height="8"/>
      <text class="brand-name" x="129" y="273">Ridgeline Auto</text>
    </svg>
  </section>

  <!-- Vision -->
  <section class="print print--vision" aria-label="Vision">
    <svg viewBox="0 0 217 288" preserveAspectRatio="none">
      <rect class="accent-fill" x="0" y="0" width="217" height="232"/>
      <polygon class="paper-fill" points="149,0 161,0 145,52 133,52"/>
      <polygon class="paper-fill" points="0,52 150,52 133,110 0,110"/>
      <polygon class="paper-fill" points="97,175 109,175 92,232 80,232"/>
      <polygon class="paper-fill" points="0,206 103,206 96,232 0,232"/>
      <rect class="paper-fill" x="0" y="232" width="217" height="56"/>
      <polygon class="shadow-fill" points="183,70 190,66 140,288 124,288"/>
      <polygon class="paper-fill" points="190,66 217,150 217,288 138,288"/>
      <rect class="frame-line" x="7" y="7" width="203" height="274"/>
      <text class="heading" x="15" y="94">VISION</text>
      <line class="heading-rule" x1="15" y1="100" x2="70" y2="100"/>
      <text class="statement" x="14" y="128">
        <tspan x="14">We will earn our reputation for being</tspan>
        <tspan x="14" dy="7">the number one, family focused,</tspan>
        <tspan x="14" dy="7">automotive specialists throughout</tspan>
        <tspan x="14" dy="7">the Latrobe Valley.</tspan>
      </text>
      <rect class="brand-mark" x="118" y="266" width="8" height="8"/>
      <text class="brand-name" x="129" y="273">Ridgeline Auto</text>
    </svg>
  </section>

  <!-- Mission -->
  <section class="print print--mission" aria-label="Mission">
    <svg viewBox="0 0 217 288" preserveAspectRatio="none">
      <rect class="accent-fill" x="0" y="0" width="217" height="232"/>
      <polygon class="paper-fill" points="149,0 161,0 145,52 133,52"/>
      <polygon class="paper-fill" points="0,52 150,52 133,110 0,110"/>
      <polygon class="paper-fill" points="97,175 109,175 92,232 80,232"/>
      <polygon class="paper-fill" points="0,206 103,206 96,232 0,232"/>
      <rect class="paper-fill" x="0" y="232" width="217" height="56"/>
      <polygon class="shadow-fill" points="183,70 190,66 140,288 124,288"/>
      <polygon class="paper-fill" points="190,66 217,150 217,288 138,288"/>
      <rect class="frame-line" x="7" y="7" width="203" height="274"/>
      <text class="heading" x="15" y="94">MISSION</text>
      <line class="heading-rule" x1="15" y1="100" x2="82" y2="100"/>
      <text class="statement statement--dense" x="14" y="125">
        <tspan x="14">Through the delivery of high-quality automotive</tspan>
        <tspan x="14" dy="5.6">services and costumer experience excellence, we</tspan>
        <tspan x="14" dy="5.6">will instil confidence and security into our clients.</tspan>
        <tspan x="14" dy="5.6">We will build a solid platform of trust in which</tspan>
        <tspan x="14" dy="5.6">our entire industry will recognise the benefits</tspan>
      </text>
      <rect class="brand-mark" x="118" y="266" width="8" height="8"/>
      <text class="brand-name" x="129" y="273">Ridgeline Auto</text>
    </svg>
  </section>

  <!-- Cultural Values -->
  <section class="print print--values" aria-label="Cultural Values">
    <svg viewBox="0 0 217 288" preserveAspectRatio="none">
      <rect class="accent-fill" x="0" y="0" width="217" height="232"/>
      <polygon class="paper-fill" points="149,0 161,0 148,44 136,44"/>
      <polygon class="paper-fill" points="0,44 153,44 120,180 0,180"/>
      <polygon class="paper-fill" points="0,222 101,222 96,232 0,232"/>
      <polygon class="paper-fill" points="98,180 110,180 92,232 80,232"/>
      <rect class="paper-fill" x="0" y="232" width="217" height="56"/>
      <polygon class="shadow-fill" points="183,70 190,66 140,288 124,288"/>
      <polygon class="paper-fill" points="190,66 217,150 217,288 138,288"/>
      <rect class="frame-line" x="7" y="7" width="203" height="274"/>
      <text class="heading" x="15" y="70">CULTURAL</text>
      <text class="heading" x="15" y="96">VALUES</text>
      <line class="heading-rule" x1="15" y1="102" x2="98" y2="102"/>
      <text class="values-list" x="15" y="132">
        <tspan x="15">-Honesty</tspan>
        <tspan x="15" dy="8">-Respect</tspan>
        <tspan x="15" dy="8">-Diligence</tspan>
        <tspan x="15" dy="8">-Pride</tspan>
      </text>
      <circle class="handshake-badge" cx="28" cy="201" r="11" role="img" aria-label="Handshake emblem in a circle"/>
      <rect class="brand-mark" x="118" y="266" width="8" height="8"/>
      <text class="brand-name" x="129" y="273">Ridgeline Auto</text>
    </svg>
  </section>

</main>
</body>
</html>
```